Specialized tax accounting firm needs marketing postcard

We need a postcard design for a professional services firm called R. Desmond Plork Inc. The firm is essentially a very specialized tax accounting firm - instead of serving the end consumer, we support other public accounting firms in the area of Canadian and U.S. tax advisory and compliance (i.e. they call us on tax issues too complex for the general practitioner). Our byline is "Tax Support Services for Public Accounting Firms". Our postcard should utilize our logo and be based on colours present in our logo (see file attached). The final design needs to convey professionalism and trustworthiness (we're hired by accountants after all!) while being creative and eye-catching. Eye-catching is critical, since many prospective recipients will not have heard from me before and I want them to read the postcard.

I've attached:
The font used in the logo
The logo itself in a variety of file formats
A picture of myself for incorporation in the postcard
A sample postcard from Publisher showing the wording to be used in the postcard and the elements to be included

Please note that in including a draft postcard I don't want the designer to follow the layout as is. It just shows the basic elements I want included. The only element which should remain constant is the wording - I do want the text elements included as written - however, everything else - font, size, placement of elements, etc. is up for creative ideas.

Please note that there is much more leather background around the logo than needs to be incorporated in the letterhead.

Industry/Entity Type

Accounting

```html
<!DOCTYPE html>
<html lang="en">
<head>
<meta charset="utf-8">
<title>R. Desmond Plork Inc. – Postcard</title>
<link rel="stylesheet" href="https://fonts.googleapis.com/css2?family=Cinzel:wght@600;700&family=PT+Serif:wght@700&family=Source+Sans+3:wght@400;600;700&display=swap">
<style>
  :root {
    --stage: #ece8e1;
    --ink-black: #111111;
    --leather: #1c1c1c;
    --leather-hi: #2e2e2e;
    --orange: #f15a24;
    --amber: #f7a81b;
    --text-light: #ffffff;
    --text-dark: #111111;
    --accent-text: #f26522;
  }
  * { box-sizing: border-box; margin: 0; padding: 0; }
  html, body { width: 1200px; height: 963px; overflow: hidden; }
  body {
    background: var(--stage);
    position: relative;
    font-family: "Source Sans 3", "Helvetica Neue", Arial, sans-serif;
  }
  .postcard {
    position: absolute;
    left: 115px; top: 110px;
    width: 970px; height: 745px;
    background: #ffffff;
    overflow: hidden;
    box-shadow: 0 4px 14px rgba(0,0,0,.18);
  }
  .postcard__swoosh { position: absolute; inset: 0; width: 970px; height: 745px; }
  .headline {
    position: absolute; left: 0; right: 0; top: 30px;
    text-align: center;
    font-family: "Cinzel", "Times New Roman", serif;
    font-weight: 700;
    font-size: 38px;
    line-height: 44px;
    letter-spacing: 1px;
    color: var(--text-light);
    white-space: nowrap;
  }
  .headline .small { font-size: 30px; }
  .intro {
    position: absolute; left: 30px; top: 106px;
    font-size: 24px; line-height: 30.5px;
    color: var(--text-light);
    white-space: nowrap;
    z-index: 2;
  }
  .portrait {
    position: absolute; left: 605px; top: 90px; width: 325px; height: 466px;
    background: linear-gradient(180deg, #8a6e5c 0%, #6a5548 25%, #2b2b2e 40%, #1d1d20 100%);
    clip-path: polygon(140px 10px, 245px 10px, 250px 140px, 225px 160px, 300px 200px, 320px 300px, 325px 466px, 0 466px, 20px 320px, 60px 200px, 160px 160px, 135px 140px);
    z-index: 1;
  }
  .phone {
    position: absolute; left: 263px; top: 346px;
    font-family: "PT Serif", Georgia, serif;
    font-weight: 700; font-size: 42px;
    color: var(--text-dark);
    letter-spacing: .5px;
  }
  .pitch {
    position: absolute; left: 30px; top: 428px; width: 570px;
    font-size: 21.5px; line-height: 22.5px;
    color: var(--text-dark);
  }
  .pitch span { display: block; text-align: justify; text-align-last: justify; white-space: nowrap; }
  .pitch span:last-child { text-align-last: left; }
  .promise {
    position: absolute; left: 26px; top: 556px; width: 492px; height: 80px;
    background: var(--ink-black);
    display: flex; flex-direction: column; justify-content: center; align-items: center;
    color: var(--accent-text);
    font-size: 22px; line-height: 28px;
  }
  .promise strong { font-weight: 700; }
  .brand {
    position: absolute; left: 530px; top: 556px; width: 423px; height: 80px;
    background: linear-gradient(135deg, var(--leather-hi), var(--leather));
    display: flex; align-items: center; gap: 14px; padding: 0 18px;
  }
  .brand__mark { width: 40px; height: 40px; background: var(--orange); flex: none; }
  .brand__text { display: flex; flex-direction: column; }
  .brand__name {
    font-family: "Cinzel", "Times New Roman", serif;
    font-weight: 600; font-size: 26px; line-height: 30px;
    color: var(--text-light);
    white-space: nowrap;
  }
  .brand__byline {
    font-family: "Cinzel", "Times New Roman", serif;
    font-weight: 600; font-size: 10.5px; letter-spacing: .6px;
    color: var(--text-light);
    margin-top: 4px;
    white-space: nowrap;
  }
  .closing {
    position: absolute; left: 0; right: 0; top: 648px;
    text-align: center;
    font-size: 27px;
    color: var(--text-dark);
    white-space: nowrap;
  }
  .contact-bar {
    position: absolute; left: 0; right: 0; bottom: 0; height: 43px;
    background: var(--ink-black);
    display: flex; align-items: center; justify-content: center; gap: 8px;
    font-size: 18px; font-weight: 700;
    color: var(--text-light);
  }
  .contact-bar .sep { color: var(--amber); font-weight: 400; }
</style>
</head>
<body>
  <article class="postcard">
    <svg class="postcard__swoosh" viewBox="0 0 970 745" aria-hidden="true">
      <defs>
        <linearGradient id="leatherTone" x1="0" y1="0" x2="1" y2="1">
          <stop offset="0" stop-color="#2a2a2a"/>
          <stop offset=".5" stop-color="#1a1a1a"/>
          <stop offset="1" stop-color="#101010"/>
        </linearGradient>
      </defs>
      <path d="M0 0 H970 V335 C720 235 330 245 0 390 Z" fill="url(#leatherTone)"/>
      <path d="M0 390 C330 245 720 235 970 335 L970 328 C720 258 330 280 0 410 Z" fill="#f7a81b"/>
      <path d="M0 410 C330 280 720 258 970 328 L970 320 C720 270 330 300 0 428 Z" fill="#f15a24"/>
    </svg>

    <h1 class="headline">D<span class="small">o your clients need help with their</span> U.S. <span class="small">taxes</span>?</h1>

    <p class="intro">You probably know that U.S. citizens have to file U.S. tax returns<br>every year—even if they live in Canada. So do your clients. That’s<br>why they’re asking you if you know anyone who can help them<br>with their U.S. filings.</p>

    <div class="portrait" role="img" aria-label="Portrait photo of the firm's principal in a dark suit, arms crossed"></div>

    <p class="phone">(902) 555-0148</p>

    <p class="pitch">
      <span>Finding a tax accountant who can help with U.S. filings</span>
      <span>is tough. U.S. tax preparers have to be registered with</span>
      <span>the IRS to be eligible to prepare U.S. returns. Your client</span>
      <span>needs someone with experience, someone timely,</span>
      <span>someone charging a reasonable price.</span>
    </p>

    <div class="promise">
      <span>With a proven track record of over 15 years,</span>
      <strong>I CAN DELIVER</strong>
    </div>

    <div class="brand">
      <span class="brand__mark"></span>
      <div class="brand__text">
        <span class="brand__name">R. Desmond Plork Inc.</span>
        <span class="brand__byline">Tax Support Services for Public Accounting Firms</span>
      </div>
    </div>

    <p class="closing">Feel free to pass along my contact information to your clients. I’d be glad to chat.</p>

    <footer class="contact-bar">
      <span>18-410 Harbourview Road, Westbridge, NS B3X 4K7</span>
      <span class="sep">|</span>
      <span>desmond@plorktax.services</span>
      <span class="sep">|</span>
      <span>www.plorktax.services</span>
    </footer>
  </article>
</body>
</html>
```